Design the best looking box truck wrap in town for an insulation and whole house fan contractor.

I would like to update my vehicle wrap look for Marlow Power Systems. Our main products are insulation and whole house fans.
I got my car wrapped recently and would like to adopt a similar look to it.

I thought it important to include a picture of my current wrap design and what I don’t like about it so as to show more what I’m looking for.
I’m looking for a more simple design.

Target Market(s)

High End Homeowners

Industry/Entity Type

Marlow power systems

Colors
0054AA
0677BA
7BADD7
CADEEF
E8F1F8
59FF00
82FF00
B8FF75
E3FFCB
F4FFEA

Requirements
Must have
• Logo as the Focal point. Insulation & Whole House fans. 482-316-9027 KRT5830196
Nice to have
• The logo as the focal point that stands out the most.
Should not have
• Pictures. Any services other than insulation and whole house fans

```html
<!DOCTYPE html>
<html lang="en">
<head>
<meta charset="utf-8">
<title>Marlow Power Systems – Box Truck Wrap</title>
<link rel="stylesheet" href="https://fonts.googleapis.com/css2?family=Questrial&family=Yellowtail&display=swap">
<style>
  :root {
    --navy: #1d3f8a;
    --blue: #2a55b0;
    --green: #8cd12e;
    --green-dark: #6fb51c;
    --white: #ffffff;
    --page: #eef1f5;
    --ink: #1d3f8a;
  }
  html, body {
    margin: 0;
    padding: 0;
    overflow: hidden;
    background: var(--page);
  }
  .canvas {
    position: relative;
    width: 1200px;
    height: 591px;
    overflow: hidden;
    background: var(--page);
    font-family: "Questrial", sans-serif;
  }
  .panel {
    position: absolute;
    display: block;
    box-shadow: 0 2px 6px rgba(0,0,0,0.18);
  }
  .side-blue  { left: 20px;  top: 22px;  width: 560px; height: 241px; }
  .side-white { left: 620px; top: 22px;  width: 560px; height: 241px; }
  .rear-blue  { left: 20px;  top: 305px; width: 260px; height: 246px; }
  .header-blue  { left: 320px; top: 330px; width: 260px; height: 100px; }
  .rear-white { left: 620px; top: 305px; width: 260px; height: 246px; }
  .header-white { left: 920px; top: 330px; width: 260px; height: 100px; }
  .brand { font-family: "Questrial", sans-serif; letter-spacing: 1px; }
  .tagline { font-family: "Yellowtail", cursive; }
  .service { font-family: "Questrial", sans-serif; }
</style>
</head>
<body>
<main class="canvas">

  <!-- Side panel, blue scheme -->
  <svg class="panel side-blue" viewBox="0 0 780 335" aria-label="Box side wrap, blue scheme">
    <rect width="780" height="335" fill="var(--navy)"/>
    <path d="M600,0 H780 V250 C700,210 630,120 600,0 Z" fill="var(--green)" stroke="var(--white)" stroke-width="4"/>
    <path d="M0,150 C160,270 460,300 780,262 V335 H0 Z" fill="var(--green)" stroke="var(--white)" stroke-width="5"/>
    <circle class="brand-mark" cx="390" cy="80" r="32" fill="var(--green)"/>
    <text class="brand" x="390" y="178" text-anchor="middle" font-size="38" fill="var(--white)">MARLOW POWER SYSTEMS</text>
    <text class="tagline" x="390" y="238" text-anchor="middle" font-size="30" fill="var(--white)">Feel The Difference</text>
    <text class="service" x="390" y="318" text-anchor="middle" font-size="19" fill="var(--navy)">Insulation &amp; Whole House Fans  482-316-9027  KRT5830196</text>
  </svg>

  <!-- Side panel, white scheme -->
  <svg class="panel side-white" viewBox="0 0 780 335" aria-label="Box side wrap, white scheme">
    <rect width="780" height="335" fill="var(--white)"/>
    <path d="M0,0 H160 C130,120 80,220 0,280 Z" fill="var(--green)" stroke="var(--navy)" stroke-width="4"/>
    <path d="M0,290 C260,300 560,250 780,150 V335 H0 Z" fill="var(--navy)" stroke="var(--green)" stroke-width="5"/>
    <circle class="brand-mark" cx="420" cy="80" r="32" fill="var(--green)"/>
    <text class="brand" x="420" y="178" text-anchor="middle" font-size="38" fill="var(--blue)">MARLOW POWER SYSTEMS</text>
    <text class="tagline" x="420" y="238" text-anchor="middle" font-size="30" fill="var(--navy)">Feel The Difference</text>
    <text class="service" x="410" y="318" text-anchor="middle" font-size="19" fill="var(--white)">Insulation &amp; Whole House Fans  482-316-9027  KRT5830196</text>
  </svg>

  <!-- Rear door, blue scheme -->
  <svg class="panel rear-blue" viewBox="0 0 380 360" aria-label="Rear door wrap, blue scheme">
    <rect width="380" height="360" fill="var(--navy)"/>
    <path d="M0,210 C120,250 270,240 380,180 V360 H0 Z" fill="var(--green)" stroke="var(--white)" stroke-width="5"/>
    <circle class="brand-mark" cx="190" cy="65" r="28" fill="var(--green)"/>
    <text class="brand" x="190" y="145" text-anchor="middle" font-size="26" fill="var(--white)">MARLOW POWER SYSTEMS</text>
    <text class="tagline" x="190" y="195" text-anchor="middle" font-size="22" fill="var(--white)">Feel The Difference</text>
    <text class="service" x="190" y="295" text-anchor="middle" font-size="19" fill="var(--navy)">Insulation &amp; Whole House Fans</text>
    <text class="service" x="190" y="325" text-anchor="middle" font-size="19" fill="var(--navy)">482-316-9027 • KRT5830196</text>
  </svg>

  <!-- Front header, blue scheme -->
  <svg class="panel header-blue" viewBox="0 0 260 100" aria-label="Box front header, blue scheme">
    <rect width="260" height="100" fill="var(--navy)"/>
    <text class="service" x="130" y="32" text-anchor="middle" font-size="17" fill="var(--white)">Insulation &amp;</text>
    <text class="service" x="130" y="55" text-anchor="middle" font-size="17" fill="var(--white)">Whole House Fans</text>
    <text class="service" x="130" y="80" text-anchor="middle" font-size="19" font-weight="700" fill="var(--white)">482-316-9027</text>
  </svg>

  <!-- Rear door, white scheme -->
  <svg class="panel rear-white" viewBox="0 0 380 360" aria-label="Rear door wrap, white scheme">
    <rect width="380" height="360" fill="var(--navy)"/>
    <path d="M0,0 H380 V180 C270,245 120,250 0,200 Z" fill="var(--white)" stroke="var(--green)" stroke-width="5"/>
    <circle class="brand-mark" cx="190" cy="65" r="28" fill="var(--green)"/>
    <text class="brand" x="190" y="145" text-anchor="middle" font-size="26" fill="var(--blue)">MARLOW POWER SYSTEMS</text>
    <text class="tagline" x="190" y="195" text-anchor="middle" font-size="22" fill="var(--navy)">Feel The Difference</text>
    <text class="service" x="190" y="295" text-anchor="middle" font-size="19" fill="var(--white)">Insulation &amp; Whole House Fans</text>
    <text class="service" x="190" y="325" text-anchor="middle" font-size="19" fill="var(--white)">482-316-9027 • KRT5830196</text>
  </svg>

  <!-- Front header, white scheme -->
  <svg class="panel header-white" viewBox="0 0 260 100" aria-label="Box front header, white scheme">
    <rect width="260" height="100" fill="var(--navy)"/>
    <text class="service" x="130" y="32" text-anchor="middle" font-size="17" fill="var(--white)">Insulation &amp;</text>
    <text class="service" x="130" y="55" text-anchor="middle" font-size="17" fill="var(--white)">Whole House Fans</text>
    <text class="service" x="130" y="80" text-anchor="middle" font-size="19" font-weight="700" fill="var(--white)">482-316-9027</text>
  </svg>

</main>
</body>
</html>
```